依頼詳細
【 デザインイメージ 】
・主に男性向けで、高級感がある、尿酸サプリにしたいです。
・ターゲット層:50~60代の男性
・色のイメージ 黄色か・金色 + α
・商品画像をパッと見て 「高級感」「イメージしやすさ」「しっかり入っていそう」とわかりやすいもの

※本品は「機能性表示食品」です そのため恐れ入りますが、暮らし安全局からの差し戻しにより、
軽微なテキスト修正などが、半年間ほどの間に2回ほど発生する可能性があります

・詳細は添付ファイルをご参考ください。
【 依頼内容 】
・ラベル ラベルサイズ 縦110 * 横80 (白いアルミチャック袋にラベルを貼ります)

・詳細は添付ファイルをご参考ください。

▼重要視する点・経験
・サプリメント、化粧品等のパッケージデザインをした経験

▼注意点・禁止事項
※他で登録されているデザインや商標の転用など、他社の知的財産権、著作権を侵すこと
※他のクライアントへ既に提案した内容の転用など

作成して頂くパッケージのデザインについてご質問等ありましたら、お気軽にご連絡下さい。
たくさんのデザイナー・クリエイターの方々からの応募をお待ちしております!
希望イメージ
シンプル 複雑
単色 カラフル
暗い 明るい
日常 高級
遊び心 厳粛
未来的 伝統的
女性的 男性的
希望する色
青系、黄・オレンジ系、尿酸なので、黄色がイメージしやすいと思っています… 詳細は添付資料をご覧ください
納品ファイル
• 高解像度JPG (.jpg)
• イラストレーター形式 (.ai)
補足説明
■ 選んだ理由

どのご提案も弊社の希望を盛り込んで頂いておりましたが、こちらのデザイン案は、
社内で「男性票」が一番多く入り、希望したテイストに仕上がっていた点が採用の決め手になりました。

■ 提案者全員のお礼・コメント

この度は多数のご提案ありがとうございました!
機能性表示食品の「規定」もある程度ふまえて選択させていただきましたが
どのデザイン案も素敵なものばかりでした。
また機会がございましたらよろしくお願い申し上げます。

```html
<!DOCTYPE html>
<html lang="ja">
<head>
<meta charset="utf-8">
<title>尿酸クリアケア ラベル</title>
<link href="https://fonts.googleapis.com/css2?family=Noto+Sans+JP:wght@400;500;700;900&family=Noto+Serif+JP:wght@700;900&display=swap" rel="stylesheet">
<style>
:root{
  --black:#0c0c0c;
  --panel:#ffffff;
  --ink:#1a1a1a;
  --gold-light:#f6e3a6;
  --gold:#c9a24a;
  --gold-dark:#8a6a22;
  --red:#c1121c;
  --red-dark:#7e0a10;
  --white:#ffffff;
}
*{margin:0;padding:0;box-sizing:border-box}
html,body{width:822px;height:1200px;overflow:hidden;background:var(--black)}
.label{position:relative;width:822px;height:1200px;background:radial-gradient(ellipse at 50% 35%,#262626 0%,var(--black) 70%);font-family:"Noto Sans JP",sans-serif;color:var(--white)}
.dose{position:absolute;top:150px;right:60px;font-size:17px;font-weight:500;color:#d8d8d8}
.lead{position:absolute;top:190px;left:60px;right:60px;text-align:center;padding:14px 0 10px;border-top:3px solid var(--gold);border-bottom:3px solid var(--gold);font-size:62px;font-weight:900;letter-spacing:1px;line-height:1.15;white-space:nowrap}
.gold-text{background:linear-gradient(180deg,var(--gold-light) 0%,var(--gold) 45%,var(--gold-dark) 55%,var(--gold) 80%,var(--gold-light) 100%);-webkit-background-clip:text;background-clip:text;color:transparent;font-weight:900}
.main-1{position:absolute;top:300px;left:0;right:0;text-align:center;font-size:136px;line-height:1.1;letter-spacing:2px;white-space:nowrap}
.main-2{position:absolute;top:455px;left:270px;font-size:150px;line-height:1.1;letter-spacing:4px;white-space:nowrap}
.ingredient{position:absolute;top:480px;left:62px;width:176px;padding:12px 8px;background:linear-gradient(180deg,var(--red) 0%,var(--red-dark) 100%);border:3px solid var(--gold);text-align:center;font-family:"Noto Serif JP",serif;font-weight:900;font-size:26px;line-height:1.3}
.chevrons{position:absolute;top:612px;left:62px;width:176px;height:120px}
.product-name{position:absolute;top:648px;left:418px;font-size:48px;line-height:1.1;font-weight:900;color:var(--red);letter-spacing:1px;white-space:nowrap}
.count{position:absolute;top:738px;right:60px;font-size:24px;font-weight:700;line-height:1.2;white-space:nowrap}
.count b{font-size:34px}
.info{position:absolute;top:790px;left:50px;right:50px;bottom:60px;background:var(--panel);color:var(--ink);padding:22px 26px;font-size:22px;line-height:1.55}
.claim{font-weight:500}
.claim-tag{font-weight:700}
.meta{display:flex;align-items:center;gap:22px;margin:16px 0 18px}
.category{background:var(--ink);color:var(--white);font-weight:700;padding:4px 14px;font-size:22px}
.notice-no{font-size:18px}
.disclaimer{font-size:17px;line-height:1.6}
</style>
</head>
<body>
<main class="label">
  <p class="dose">1日摂取目安量3粒</p>
  <h2 class="lead">尿酸値が高めな方の</h2>
  <h1>
    <span class="main-1 gold-text">尿酸値を</span>
    <span class="main-2 gold-text">下げる</span>
  </h1>
  <div class="ingredient">菊の花由来<br>ルテオリン<br>配合</div>
  <svg class="chevrons" viewBox="0 0 176 120" aria-hidden="true">
    <defs>
      <linearGradient id="chevron-gold" x1="0" y1="0" x2="0" y2="1">
        <stop offset="0" stop-color="#f6e3a6"/>
        <stop offset="0.5" stop-color="#c9a24a"/>
        <stop offset="1" stop-color="#8a6a22"/>
      </linearGradient>
    </defs>
    <polygon points="0,0 88,40 176,0 176,30 88,70 0,30" fill="url(#chevron-gold)"/>
    <polygon points="0,50 88,90 176,50 176,80 88,120 0,80" fill="url(#chevron-gold)"/>
  </svg>
  <p class="product-name">尿酸クリアケア</p>
  <p class="count"><b>90</b>粒 約1ヶ月分入</p>
  <section class="info">
    <p class="claim"><span class="claim-tag">【届出表示】</span>本品には、(菊の花由来)ルテオリンが含まれます。ルテオリンには尿酸値が高めな方の尿酸値を下げる機能が報告されています。</p>
    <div class="meta">
      <span class="category">機能性表示食品</span>
      <span class="notice-no">届出番号／0000</span>
    </div>
    <p class="disclaimer">本品は、事業者の責任において特定の保健の目的が期待できる旨を表示するものとして、暮らし安全局長官に届出されたものです。ただし、特定保健用食品と異なり、暮らし安全局長官による個別審査を受けたものではありません。</p>
  </section>
</main>
</body>
</html>
```